Bramble Systems Voip Broucher

We require a full page broucher 8.5X11 format for a Voip promotion
Updates

Target Market(s)

Business Customer

Industry/Entity Type

Voip

Colors
ec1f27
0592cd

Requirements
Must have
• Logo, Information as provided, our phone number 1-877-555-0193, Colors that match the logo. Reds, blues and white please.

```html
<!DOCTYPE html>
<html lang="en">
<head>
<meta charset="utf-8">
<title>Bramble Systems VoIP Brochure</title>
<link href="https://fonts.googleapis.com/css2?family=Archivo:wght@400;700;800&family=Arimo:wght@400;700&display=swap" rel="stylesheet">
<style>
:root{
  --backdrop:#b9bbbd;
  --paper:#ffffff;
  --brick:#b3553f;
  --brick-deep:#9c4430;
  --sky:#1e93d2;
  --sky-deep:#1780bf;
  --pale:#eef1f4;
  --red:#c0392b;
  --ink:#1e1e1e;
  --white:#ffffff;
}
*{margin:0;padding:0;box-sizing:border-box}
html,body{width:1200px;height:1000px;overflow:hidden;background:var(--backdrop)}
.brochure{position:absolute;left:253px;top:52px;width:693px;height:896px;background:var(--paper);overflow:hidden;font-family:"Arimo",Arial,sans-serif;color:var(--white)}
.backdrop-shapes{position:absolute;inset:0}
.abs{position:absolute}
.brand{left:28px;top:46px;font-family:"Archivo",Arial,sans-serif;font-weight:800;font-size:19px;line-height:22px;color:var(--red);letter-spacing:.2px;display:flex;align-items:center;gap:7px;white-space:nowrap}
.brand-mark{width:12px;height:12px;background:var(--red)}
.support{left:260px;top:43px;width:353px;height:41px;border:3px solid var(--white);border-radius:9px;display:flex;align-items:center;padding:3px;white-space:nowrap}
.support-label{background:var(--sky);height:100%;width:132px;flex:none;border-radius:5px;display:flex;align-items:center;justify-content:flex-end;padding-right:8px;font-family:"Archivo",Arial,sans-serif;font-weight:700;font-size:17px}
.support-number{font-family:"Archivo",Arial,sans-serif;font-weight:800;font-size:21px;line-height:1;margin-left:14px;letter-spacing:.3px;white-space:nowrap}
.headline{left:102px;top:168px;font-family:"Archivo",Arial,sans-serif;font-weight:800;font-size:24.5px;line-height:25.5px;letter-spacing:.5px;text-transform:uppercase}
.headline-rule{left:81px;top:165px;width:2px;height:166px;background:var(--white)}
.section-title{display:flex;align-items:center;gap:10px;font-family:"Archivo",Arial,sans-serif;font-weight:800;font-size:19px;color:var(--red);letter-spacing:.3px;white-space:nowrap}
.get-title{left:384px;top:232px}
.cost-title{left:0;top:533px}
.qa-title{left:207px;top:815px}
.features{left:348px;top:280px;width:290px;list-style:none}
.features li,.costs li{position:relative;padding-left:12px;font-weight:700;font-size:12.6px;line-height:15px;text-transform:uppercase;margin-bottom:10px}
.features li::before,.costs li::before{content:"";position:absolute;left:0;top:4px;width:7px;height:7px;border-radius:50%;background:var(--white)}
.features .detail,.costs .detail{display:block;font-weight:400;text-transform:none;font-size:12.6px}
.features .gap{margin-top:20px}
.costs{left:12px;top:578px;width:302px;list-style:none}
.costs li{margin-bottom:14px}
.handset{left:515px;top:458px;width:170px;height:130px;border-radius:8px;background:linear-gradient(160deg,#3a3d42,#15171a)}
.divider{width:1px;background:#cfd4d9}
.qa{font-size:8.4px;line-height:10px;color:var(--ink)}
.qa p{margin-bottom:9px}
.qa-left{left:352px;top:736px;width:160px}
.qa-right{left:528px;top:617px;width:160px}
</style>
</head>
<body>
<main class="brochure">
  <svg class="backdrop-shapes" width="693" height="896" viewBox="0 0 693 896" aria-hidden="true">
    <defs>
      <linearGradient id="brickShade" x1="0" y1="0" x2="1" y2="1">
        <stop offset="0" stop-color="#b95c45"/><stop offset="1" stop-color="#9f4a36"/>
      </linearGradient>
      <linearGradient id="skyShade" x1="0" y1="0" x2="0" y2="1">
        <stop offset="0" stop-color="#1f96d4"/><stop offset="1" stop-color="#1a86c6"/>
      </linearGradient>
      <linearGradient id="paleShade" x1="0" y1="0" x2="1" y2="1">
        <stop offset="0" stop-color="#dfe6ec"/><stop offset="1" stop-color="#f7f8fa"/>
      </linearGradient>
    </defs>
    <polygon points="312,0 515,0 0,470 0,225" fill="url(#brickShade)"/>
    <polygon points="515,0 693,0 693,445 333,740 333,896 0,896 0,470" fill="url(#skyShade)"/>
    <polygon points="693,445 693,896 333,896 333,740" fill="url(#paleShade)"/>
    <polygon points="0,300 200,300 0,500" fill="#ffffff" opacity=".06"/>
  </svg>
  <div class="abs" role="img" aria-label="Photo of office tower facades behind the diagonal colour bands" style="inset:0;pointer-events:none"></div>

  <div class="abs brand"><span class="brand-mark"></span>Bramble Systems</div>

  <div class="abs support">
    <div class="support-label">SUPPORT</div>
    <div class="support-number">1-877-555-0193</div>
  </div>

  <div class="abs headline-rule"></div>
  <h1 class="abs headline">Upgrade your<br>office phone<br>system and<br>cut your<br>phone bill<br>in half</h1>

  <h2 class="abs section-title get-title">
    <svg width="42" height="40" viewBox="0 0 42 40" aria-hidden="true"><polygon points="0,11 22,11 22,0 42,20 22,40 22,29 0,29" fill="var(--red)"/></svg>
    WHAT DO YOU GET?
  </h2>
  <ul class="abs features">
    <li>Modern office phone system with the latest features only available through Voice over IP</li>
    <li>Installation and ongoing support services as required</li>
    <li>Unlimited local and long distance calling within North America only</li>
    <li class="gap">Included phone feature set:<span class="detail">Auto attendant, Voicemail,<br>3 ways calling, hands free,<br>call forward, Intercom,<br>email tie in.</span></li>
    <li>Support services:<span class="detail">hardware installation,<br>training,<br>ongoing support,</span></li>
  </ul>

  <div class="abs handset" role="img" aria-label="Photo of a black colour-screen desk phone"></div>

  <h2 class="abs section-title cost-title">
    <svg width="48" height="40" viewBox="0 0 48 40" aria-hidden="true"><polygon points="0,11 28,11 28,0 48,20 28,40 28,29 0,29" fill="var(--red)"/></svg>
    WHAT DOES IT COST?
  </h2>
  <ul class="abs costs">
    <li>Flat monthly fee of $25.00 per month per desk phone</li>
    <li>Costing for a hypothetical<span class="detail">Example:<br>Harbor Administration office has 35 office phones.<br>What will it cost to upgrade the office and<br>what will the monthly cost be?<br>$25.00 line fee x 35 handsets =<br>$875.00 per month.</span></li>
  </ul>

  <h2 class="abs section-title qa-title">
    <svg width="48" height="40" viewBox="0 0 48 40" aria-hidden="true"><polygon points="0,11 28,11 28,0 48,20 28,40 28,29 0,29" fill="var(--red)"/></svg>
    Q&amp;A
  </h2>

  <div class="abs divider" style="left:333px;top:258px;height:638px"></div>
  <div class="abs divider" style="left:518px;top:590px;height:306px"></div>

  <div class="abs qa qa-left">
    <p><b>Q</b> How does it work?<br><b>A</b> Rather than calls coming and going through Northline phone lines, calls get routed to the exchange through the internet connection.</p>
    <p><b>Q</b> Is this a new and is it reliable<br><b>A</b> This technology has been around for over a decade. Its works very well and is used across the globe.</p>
    <p><b>Q</b> Can I keep our offices existing telephone number?<br><b>A</b> Yes, we can port the existing number</p>
  </div>

  <div class="abs qa qa-right">
    <p><b>Q</b> Is there 911 services<br><b>A</b> Yes, we register your legal land description with E911 and 911 calling is available</p>
    <p><b>Q</b> Can we fax using VoIP<br><b>A</b> Yes faxing works fine through VoIP.</p>
    <p><b>Q</b> What does it cost to upgrade the handset to a colour display phone that supports video calling?<br><b>A</b> one-time fee of $100 per handset to move to colour. Colour handsets also supports video calling</p>
    <p><b>Q</b> What costs are not included to get the new phone system in place.<br><b>A</b> The new phone system run through ethernet office network cabling. Your office may need the cabling upgraded to allow use of VoIP phones. We can provide an affordable estimate to improve your cabling to support a VoIP phone.<br><b>A</b> The calls will route through your existing office internet connection.</p>
  </div>
</main>
</body>
</html>
```